Brellin Trade Partners - we are Asian sourcing agents

We are sourcing agents based in the USA and we act as sourcing agents for clients in throughout the world. We focus primarily on custom sewn goods. So basically companies who do not have the in-house expertise to do it themselves, come to us and have us find suitable factories in Asia to do the production. We are middlemen. We find the factories...quote the project...manage the quality control and then deliver the goods directly to our customer's door. We pride ourselves in making the communication very easy and precise.

Current page is www.brellintrade.example

I am not happy w/ the overall look. The spacing...the photos, the fonts...the design elements...the pictures. I want a cool, crisp design that conveys professionalism and clearly depicts/explains what we do.

Requirements
Must have
• use my logo....I like it...it was designed by someone on this website.
Nice to have
• a video/animation of the entire process would be wonderful. Showing initial contact with our office in the USA...then to my correspondence with my offices in Taiwan and in Hong Kong...and then back and fort w/ the customer.....and then between my people in Hong Kong/Taiwan with the local factories......and then a quote is generated and sent to my client......to samples being made and sent for approval.....to a PO being generated......to final samples being sent.....to the order being shipped and delivered to the clients warehouse. I was thinking of an animation showing arrows and text showing the back and forth communication and explaining how the process flows.

```html
<!DOCTYPE html>
<html lang="en">
<head>
<meta charset="utf-8">
<title>Brellin Trade Partners – Asian Outsourcing Made Easy</title>
<link href="https://fonts.googleapis.com/css2?family=Open+Sans:wght@400;600;700;800&display=swap" rel="stylesheet">
<style>
:root{
  --green:#6ab023;
  --green-dark:#4f8e14;
  --navy:#0c1f3a;
  --navy-2:#13294a;
  --ink:#2b2b2b;
  --muted:#777;
  --paper:#ffffff;
  --grey-bar:#8a8a8a;
  --light:#f3f3f3;
}
*{box-sizing:border-box;margin:0;padding:0}
html,body{width:1200px;height:2636px;overflow:hidden}
body{font-family:"Open Sans",Arial,sans-serif;color:var(--ink);background:var(--paper);position:relative}
.wordmark{font-weight:800;color:var(--navy);font-size:26px;line-height:1;display:flex;align-items:center;gap:10px}
.wordmark .dot{width:14px;height:14px;background:var(--green);border-radius:50%}

/* header */
.site-header{height:120px;display:flex;align-items:center;justify-content:space-between;padding:0 60px 0 90px}
.header-right{display:flex;flex-direction:column;align-items:flex-end;gap:10px}
.tollfree{font-size:14px;color:var(--muted)}
.tollfree b{color:var(--ink)}
.main-nav{display:flex;gap:6px}
.main-nav a{font-size:14px;font-weight:600;color:var(--ink);text-decoration:none;padding:8px 14px}
.main-nav a.active{background:var(--green);color:#fff}

/* hero */
.hero{position:relative;height:440px;background:linear-gradient(100deg,#3c4a1f 0%,#7f9a3a 38%,#c9d7a6 65%,#8b8f86 100%)}
.hero-copy{position:absolute;left:110px;top:120px}
.hero h1{font-size:62px;line-height:1.05;font-weight:800;color:#fff}
.hero h1 span{color:var(--green)}
.hero .tagline{display:inline-block;margin-top:12px;background:var(--green);color:#fff;font-weight:600;font-size:18px;padding:6px 14px}
.btn-dark{display:inline-block;margin-top:20px;background:var(--navy);color:#fff;font-weight:700;font-size:16px;padding:12px 26px;text-decoration:none}

/* services */
.services{height:560px;background:var(--light);padding-top:50px;text-align:center}
.section-title{font-size:40px;font-weight:700;color:var(--ink)}
.section-title span{color:var(--green)}
.title-rule{width:520px;height:2px;background:var(--green);margin:10px auto 0}
.service-row{display:flex;justify-content:center;gap:40px;margin-top:40px}
.service-card{width:200px;text-align:left}
.service-photo{width:150px;height:150px;border-radius:50%;border:6px solid #fff;box-shadow:0 0 0 2px #ccc;margin:0 auto;background:radial-gradient(circle,#b9b9b9,#555)}
.service-card h3{margin-top:22px;font-size:19px;font-weight:700;color:var(--ink);border-top:1px solid #bbb;padding-top:6px}
.service-card .strip{display:block;background:var(--grey-bar);color:#fff;font-size:13px;padding:4px 8px;margin-top:4px}
.service-card p{font-size:12px;color:var(--muted);margin-top:14px;line-height:1.6}

/* alone band */
.alone{height:360px;background:linear-gradient(180deg,#2a2a2a,#1d1a16 60%,#3a3027);color:#ddd;text-align:center;padding-top:50px}
.alone h2{font-size:36px;font-weight:800;color:#fff}
.alone p{width:820px;margin:16px auto 0;font-size:13px;line-height:1.7}
.btn-green{display:inline-block;background:var(--green);color:#fff;font-weight:600;font-size:15px;padding:9px 20px;text-decoration:none;margin-top:24px}

/* know + video */
.know-video{height:552px;display:flex;padding:60px 40px 0 70px;gap:40px}
.know{width:460px}
.know h2,.video h2{font-size:38px;font-weight:700;color:var(--green)}
.know h2 b{color:var(--navy)}
.know ul{list-style:none;margin-top:26px}
.know li{display:flex;align-items:center;gap:14px;font-size:17px;color:#444;padding:9px 0}
.video{flex:1}
.video-frame{margin-top:18px;height:390px;background:linear-gradient(135deg,#e4e4e4,#bfc3c6 45%,#6f7e8f)}

/* cta band */
.cta-band{height:80px;background:var(--navy-2);display:flex;align-items:center;justify-content:space-between;padding:0 110px;color:#fff}
.cta-band h3{font-size:22px;font-weight:700}
.cta-band p{font-size:13px;color:#c5cfdd}
.cta-band .btn-green{margin:0;font-weight:700}

/* footer */
.site-footer{height:448px;background:var(--navy);color:#9fb0c6;padding:40px 110px 0}
.footer-grid{display:grid;grid-template-columns:repeat(4,1fr);column-gap:40px;row-gap:26px}
.footer-grid h4{color:#fff;font-size:16px;font-weight:700;line-height:1.25;border-bottom:1px solid #34496a;padding-bottom:6px;margin-bottom:8px}
.footer-grid li{list-style:none;font-size:12px;line-height:1.75}
.bottom-bar{height:76px;background:#081629;display:flex;align-items:center;justify-content:space-between;padding:0 60px 0 110px;color:#8ea0b8;font-size:12px}
.bottom-bar .wordmark{color:#fff;font-size:22px}
</style>
</head>
<body>

<header class="site-header">
  <div class="wordmark"><span class="dot"></span>Brellin Trade Partners</div>
  <div class="header-right">
    <div class="tollfree">Toll Free: <b>555-014-2290</b></div>
    <nav class="main-nav">
      <a class="active" href="#">HOME</a>
      <a href="#">PRODUCT CATEGORIES</a>
      <a href="#">ABOUT US</a>
      <a href="#">REQUEST QUOTE</a>
      <a href="#">CONTACT US</a>
    </nav>
  </div>
</header>

<section class="hero" role="img" aria-label="Close-up of a sewing machine stitching green fabric">
  <div class="hero-copy">
    <h1><span>Asian</span> Outsourcing<br>Made Easy!</h1>
    <div class="tagline">Custom Sewn Goods Made to Your Specifications</div><br>
    <a class="btn-dark" href="#">LEARN MORE</a>
  </div>
</section>

<section class="services">
  <h2 class="section-title"><span>Our</span> SERVICES</h2>
  <div class="title-rule"></div>
  <div class="service-row">
    <div class="service-card">
      <div class="service-photo" role="img" aria-label="Stack of sewn textile goods"></div>
      <h3>SEWN GOODS</h3><span class="strip">Manufacturing in Asia</span>
      <p>Locating sewing manufacturers in China, India, Korea, Vietnam, Thailand to quote your custom.</p>
    </div>
    <div class="service-card">
      <div class="service-photo" role="img" aria-label="Custom bag sample"></div>
      <h3>CUSTOM BAG</h3><span class="strip">Manufacturing in Asia</span>
      <p>We can accommodate any material request that you may have leather, polyester, nylon, PVC, cotton.</p>
    </div>
    <div class="service-card">
      <div class="service-photo" role="img" aria-label="Hands wearing custom gloves"></div>
      <h3>CUSTOM GLOVE</h3><span class="strip">Manufacturing in Asia</span>
      <p>We provide a comprehensive service from initial design, raw material sourcing, sample development.</p>
    </div>
    <div class="service-card">
      <div class="service-photo" role="img" aria-label="Equipment cover on a machine"></div>
      <h3>CUSTOM COVER</h3><span class="strip">Manufacturing in Asia</span>
      <p>Our team has been helping our clients with their custom cover needs since 1996.</p>
    </div>
  </div>
</section>

<section class="alone">
  <h2>DON'T GO AT IT ALONE!</h2>
  <p>Brellin Trade Partners has been sourcing custom sewn goods in Asia since 1996. We work with our clients by matching their unique production needs with the best possible sewing factories. We manage the entire process from start to finish, by first identifying the best factories to quote each job. The next step is negotiating the best price possible. We complete the process by monitoring the quality of the goods during production, and then managing</p>
  <p>the ocean logistics, customs clearance and local delivery right to your door. Our services and our total commitment to customer satisfaction help level the playing field by giving our customers access to low cost.</p>
  <a class="btn-green" href="#">Read More</a>
</section>

<section class="know-video">
  <div class="know">
    <h2>What you need to <b>KNOW ?</b></h2>
    <ul>
      <li><svg width="22" height="22" viewBox="0 0 22 22"><circle cx="11" cy="11" r="11" fill="#6ab023"/><path d="M6 11.5l3.3 3.3L16 8" stroke="#fff" stroke-width="2.4" fill="none"/></svg>Contract Sewing in China</li>
      <li><svg width="22" height="22" viewBox="0 0 22 22"><circle cx="11" cy="11" r="11" fill="#6ab023"/><path d="M6 11.5l3.3 3.3L16 8" stroke="#fff" stroke-width="2.4" fill="none"/></svg>What is the process ?</li>
      <li><svg width="22" height="22" viewBox="0 0 22 22"><circle cx="11" cy="11" r="11" fill="#6ab023"/><path d="M6 11.5l3.3 3.3L16 8" stroke="#fff" stroke-width="2.4" fill="none"/></svg>What is the minimum Order ?</li>
      <li><svg width="22" height="22" viewBox="0 0 22 22"><circle cx="11" cy="11" r="11" fill="#6ab023"/><path d="M6 11.5l3.3 3.3L16 8" stroke="#fff" stroke-width="2.4" fill="none"/></svg>Contract Outsourcing FAQ</li>
      <li><svg width="22" height="22" viewBox="0 0 22 22"><circle cx="11" cy="11" r="11" fill="#6ab023"/><path d="M6 11.5l3.3 3.3L16 8" stroke="#fff" stroke-width="2.4" fill="none"/></svg>Outsourcing Case Study</li>
      <li><svg width="22" height="22" viewBox="0 0 22 22"><circle cx="11" cy="11" r="11" fill="#6ab023"/><path d="M6 11.5l3.3 3.3L16 8" stroke="#fff" stroke-width="2.4" fill="none"/></svg>Custom Industrial Sewing in China</li>
    </ul>
  </div>
  <div class="video">
    <h2>Our VIDEO</h2>
    <div class="video-frame" role="img" aria-label="Hands holding a tablet playing the sourcing process video"></div>
  </div>
</section>

<section class="cta-band">
  <div>
    <h3>Outsource Your Sewing Needs to Trusted Contractors in China</h3>
    <p>Please contact us for immediate consultation regarding your outsourcing project.</p>
  </div>
  <a class="btn-green" href="#">GET A QUOTE &gt;&gt;</a>
</section>

<footer class="site-footer">
  <div class="footer-grid">
    <div><h4>CUSTOM BAGS</h4><ul><li>Athletic Bags</li><li>Backpacks</li><li>Computer Bags</li><li>Cooler Bags</li><li>Cosmetic Bags</li><li>Handbags</li><li>Messenger Bags</li></ul></div>
    <div><h4>CUSTOM COVERS</h4><ul><li>ATV Covers</li><li>Chair Covers</li><li>Equipment Covers</li><li>Golf Cart Covers</li><li>Motorcycle Covers</li><li>Outdoor Furniture Covers</li><li>Outdoor Grill Covers</li></ul></div>
    <div><h4>CUSTOM MEDICAL ACCESSORIES</h4><ul><li>Medical Equipment Covers</li><li>Medical Pouches</li><li>Medical Straps &amp; Webbing</li><li>Supplies</li><li>Oxygen Tank Carry Bags</li></ul></div>
    <div><h4>CUSTOM GLOVES</h4><ul><li>Batting Gloves</li><li>Garden Gloves</li><li>Mechanic Gloves</li><li>Safety Gloves</li><li>Ski Gloves</li></ul></div>
    <div><h4>CUSTOM SEWN GOODS</h4><ul><li>Pet Collars, Leashes &amp; Harnesses</li><li>Belts</li></ul></div>
    <div><h4>CUSTOM SPORTING GOODS</h4><ul><li>Yoga Mats</li><li>Yoga Gear and Accessories</li></ul></div>
    <div><h4>CUSTOM CASES</h4><ul><li>Custom Cases</li><li>Phone Cases</li><li>Tool Bags and Tool Cases</li></ul></div>
    <div><h4>CONTACT US</h4><ul><li>Brellin Trade Partners, LLC</li><li>48 Harbor Lane, Suite 3</li><li>Online Inquiry Form</li><li>Tel: (555) 014-2290</li><li>Fax: (555) 014-2291</li><li>hello@brellintrade.example</li></ul></div>
  </div>
</footer>

<div class="bottom-bar">
  <span>Copyright © 2015 Brellin Trade Partners, LLC. | USA - Hong Kong - Taipei</span>
  <div class="wordmark"><span class="dot"></span>Brellin Trade Partners</div>
</div>

</body>
</html>
```